Copper Lantern Digital Advertisement

This project is a request for a unique ad picture and message for Copper Lantern that will grab the audience instantly. Copper Lantern is a turn-around specialist and mobile online marketing agency. We create sustainable digital beach-heads (brand + value prop). Our tagline = Digital Builders. Our website is located at: copperlantern-example.com

Target Market(s)

small and medium business owners and leadership team

Requirements
Must have
• Key Messages: 1) TAP INTO THE RIGHT TRAFFIC 2) "Instinct is Correct. 7 out of 10 CEOs believe they're wasting advertising & marketing money" (Halvern) 3) Copper Lantern uses a proven and trademarked algorithm for growth.

```html
<!DOCTYPE html>
<html lang="en">
<head>
<meta charset="utf-8">
<title>Copper Lantern — Digital Builders</title>
<link rel="stylesheet" href="https://fonts.googleapis.com/css2?family=Open+Sans:wght@300;400;700&display=swap">
<style>
  :root {
    --frame-grey: #636267;
    --paper: #ffffff;
    --ink: #1c1c1c;
    --photo-wood-dark: #5a3a22;
    --photo-wood-mid: #9a6a44;
    --photo-wood-light: #c9a27e;
    --photo-haze: #d8cfc6;
    --pool-blue: #3fa8d8;
    --logo-purple: #5b3f8f;
    --overlay-white: #ffffff;
  }
  * { margin: 0; padding: 0; box-sizing: border-box; }
  html, body { width: 1200px; height: 1200px; overflow: hidden; }
  body {
    background: var(--frame-grey);
    font-family: "Open Sans", Arial, sans-serif;
    position: relative;
  }
  .ad-sheet {
    position: absolute; left: 0; top: 177px;
    width: 1200px; height: 848px;
    background: var(--paper);
  }
  .hero {
    position: absolute; left: 22px; top: 22px;
    width: 1162px; height: 576px;
    overflow: hidden;
  }
  .hero-photo {
    position: absolute; inset: 0;
    background:
      radial-gradient(ellipse 340px 90px at 600px 420px, rgba(63,168,216,0.85), rgba(63,168,216,0) 100%),
      radial-gradient(ellipse 500px 220px at 700px 120px, rgba(216,207,198,0.8), rgba(216,207,198,0) 100%),
      linear-gradient(180deg, var(--photo-wood-dark) 0%, var(--photo-wood-mid) 45%, var(--photo-wood-light) 75%, var(--photo-wood-mid) 100%);
  }
  .brand-tile {
    position: absolute; left: 78px; top: 0;
    width: 175px; height: 186px;
    background: var(--paper);
    display: flex; align-items: center; justify-content: center; gap: 8px;
    flex-direction: column;
  }
  .brand-mark { width: 22px; height: 22px; background: var(--logo-purple); }
  .brand-name {
    font-weight: 700; font-size: 26px; line-height: 1.05;
    color: var(--logo-purple); text-align: center;
  }
  .headline {
    position: absolute; left: 453px; top: 48px;
    color: var(--overlay-white);
    font-weight: 400; font-size: 52px; line-height: 72px;
    transform: rotate(4deg); transform-origin: left top;
    letter-spacing: -0.5px;
  }
  .headline span { display: block; }
  .headline .line-two { margin-left: -20px; }
  .feature-icons { position: absolute; left: 405px; top: 200px; }
  .key-messages {
    position: absolute; left: 46px; bottom: 16px;
    color: var(--overlay-white);
    text-shadow: 0 1px 3px rgba(0,0,0,0.45);
  }
  .key-messages .call-out {
    font-weight: 700; font-size: 18px; letter-spacing: 1px; line-height: 24px;
  }
  .key-messages .stat {
    font-weight: 400; font-size: 14px; line-height: 20px;
  }
  .site-url {
    position: absolute; right: 46px; bottom: 16px;
    color: var(--overlay-white); font-size: 17px;
  }
  .copy {
    position: absolute; left: 104px; top: 622px; width: 1036px;
    color: var(--ink); font-size: 19px; line-height: 24px;
    text-align: justify;
  }
  .copy .tagline { font-weight: 700; margin-bottom: 24px; }
  .copy p + p { margin-top: 24px; }
</style>
</head>
<body>
  <section class="ad-sheet">
    <div class="hero">
      <div class="hero-photo" role="img" aria-label="Photo of a smartphone on a wooden desk whose screen is a pool of blue water, a swimmer sitting at its edge, earphones and a coffee cup nearby"></div>

      <div class="brand-tile">
        <span class="brand-mark"></span>
        <span class="brand-name">Copper<br>Lantern</span>
      </div>

      <h1 class="headline">
        <span class="line-one">Plunge into</span>
        <span class="line-two">big data pool.</span>
      </h1>

      <svg class="feature-icons" width="380" height="130" viewBox="0 0 380 130" aria-hidden="true"
           fill="none" stroke="#ffffff" stroke-width="2" stroke-linecap="round" stroke-linejoin="round">
        <g transform="rotate(4 40 40)">
          <rect x="5" y="5" width="70" height="70" rx="10"/>
          <circle cx="40" cy="34" r="12"/>
          <path d="M35 46v8h10v-8M36 58h8M40 14v-4M24 20l-3-3M56 20l3-3"/>
        </g>
        <g transform="translate(93 10) rotate(4 40 40)">
          <rect x="5" y="5" width="70" height="70" rx="10"/>
          <path d="M25 22c-3 3-3 8 2 15s12 14 19 17c4 2 8 0 10-3l-7-7-5 3c-4-2-9-7-11-11l3-5-7-7z"/>
          <path d="M46 24a12 12 0 0 1 10 10M48 16a20 20 0 0 1 16 16"/>
        </g>
        <g transform="translate(186 22) rotate(4 40 40)">
          <rect x="5" y="5" width="70" height="70" rx="10"/>
          <path d="M20 34l20 14 20-14v26H20z M20 34l20-14 20 14"/>
          <path d="M20 60l15-12M60 60l-15-12"/>
        </g>
        <g transform="translate(279 34) rotate(4 40 40)">
          <rect x="5" y="5" width="70" height="70" rx="10"/>
          <path d="M26 52h30a9 9 0 0 0 0-18 13 13 0 0 0-25-2 10 10 0 0 0-5 20z"/>
        </g>
      </svg>

      <div class="key-messages">
        <p class="call-out">TAP INTO THE RIGHT TRAFFIC</p>
        <p class="stat">Instinct is correct: 7 out of 10 CEOs believe they're wasting advertising &amp; marketing money. (Halvern)</p>
      </div>

      <span class="site-url">www.copperlantern-example.com</span>
    </div>

    <div class="copy">
      <p class="tagline">We are digital builders.</p>
      <p>We help entrepreneurs and independent business owners establish their mobile online presence to improve, optimize and then sustain their business performance.</p>
      <p>Copper Lantern implements digital mobile marketing and commerce platforms utilizing brilliant rich creative work and our proven, trademarked digital framework algorithm that guarantees cost savings, sustainable growth and a unique brand identity for customers.</p>
    </div>
  </section>
</body>
</html>
```